Presentation Folder

We want to create a clean, modern folder for our three companies- A single folder. Feel free to be as creative as possible. We are good with some color, but want it to stay clean and modern. See our website veltrimhire.net for more idea of the vibe. I've attached all 3 logos to be used as well as our new business cards

Target Market(s)

Senior executives

Industry/Entity Type

Business

Font styles to use
Serif
Sans Serif

Colors
85acd3
3176b5
0455a3
0792cd
34a6d7
85cae6

Requirements
Must have
• All 3 logos websites and phone numbers (see business card).

```html
<!DOCTYPE html>
<html lang="en">
<head>
<meta charset="utf-8">
<title>Presentation Folder</title>
<link rel="stylesheet" href="https://fonts.googleapis.com/css2?family=Barlow:wght@400;500;600&family=Cinzel:wght@600&display=swap">
<style>
  :root{
    --bg:#575b61;
    --navy:#0455a3;
    --navy-deep:#0a4e9a;
    --sky-soft:#1f8cca;
    --ice:#85acd3;
    --paper:#e4e4e2;
    --ink:#1b274a;
    --strip:#5b5e63;
  }
  *{margin:0;padding:0;box-sizing:border-box}
  html,body{width:1200px;height:675px;overflow:hidden}
  body{background:radial-gradient(ellipse at 50% 35%,#62666c 0%,var(--bg) 60%,#4a4e54 100%);font-family:"Barlow",Arial,sans-serif;position:relative}

  .cover{position:absolute;left:103px;top:118px;width:285px;height:445px;overflow:hidden;box-shadow:0 6px 16px rgba(0,0,0,.35)}
  .cover-head{position:absolute;left:0;top:0;width:100%;height:210px;background:linear-gradient(180deg,#0b58a6,var(--navy-deep));display:flex;flex-direction:column;justify-content:center;padding-left:44px;gap:6px}
  .motto{color:#fff;line-height:1;letter-spacing:1px;font-weight:400}
  .motto.prepare{font-size:20px}
  .motto.place{font-size:26px}
  .motto.support{font-size:15px;color:var(--ice)}
  .motto-rule{width:36px;height:2px;background:var(--ice);margin-top:4px}
  .cover-photo{position:absolute;left:0;top:210px;width:100%;height:102px;background:linear-gradient(90deg,#6c6c6c,#a9a9a9 45%,#3f8fcf 55%,#9a9a9a 70%,#777)}
  .cover-rule{position:absolute;left:0;top:312px;width:100%;height:11px;background:var(--sky-soft)}
  .brand-band{position:absolute;left:0;top:323px;width:100%;height:71px;background:var(--paper);display:flex;align-items:center;justify-content:space-around;padding:0 8px}
  .brand{display:flex;align-items:center;gap:4px;color:var(--ink);font-weight:600;font-size:9px;text-align:center;line-height:1.15;letter-spacing:.4px;max-width:82px}
  .brand-mark{width:9px;height:9px;background:var(--navy);flex:none}
  .brand-mark.round{border-radius:50%}
  .cover-foot{position:absolute;left:0;bottom:0;width:100%;height:51px;background:var(--sky-soft)}

  .spread{position:absolute;left:454px;top:134px;width:632px;height:420px;box-shadow:0 6px 16px rgba(0,0,0,.35)}
  .panel{position:absolute;top:0;height:100%;width:316px}
  .panel.left{left:0;background:linear-gradient(90deg,#8c8c8c,#858585)}
  .panel.right{left:316px;background:linear-gradient(90deg,#838383,#8b8b8b)}
  .fold{position:absolute;left:315px;top:0;width:2px;height:100%;background:#777}
  .pocket{position:absolute;left:314px;top:273px;width:318px;height:147px}
  .card{position:absolute;left:376px;top:301px;width:200px;height:113px;background:#fff;box-shadow:0 1px 3px rgba(0,0,0,.25)}
  .card-name{position:absolute;top:34px;width:100%;text-align:center;font-family:"Cinzel",Georgia,serif;font-weight:600;font-size:15px;color:var(--ink);letter-spacing:.5px}
  .card-role{position:absolute;top:54px;width:100%;text-align:center;font-family:"Cinzel",Georgia,serif;font-weight:600;font-size:11px;color:var(--ink)}
  .card-strip{position:absolute;left:0;bottom:0;width:100%;height:16px;background:var(--strip);color:#e8e8e8;font-size:8px;display:flex;align-items:center;justify-content:center;gap:4px;letter-spacing:.3px}
</style>
</head>
<body>
  <section class="cover" aria-label="Folder front cover">
    <div class="cover-head">
      <span class="motto prepare">PREPARE</span>
      <span class="motto place">PLACE</span>
      <span class="motto support">SUPPORT</span>
      <span class="motto-rule"></span>
    </div>
    <div class="cover-photo" role="img" aria-label="Photo of schoolchildren gathered around a globe in a library"></div>
    <div class="cover-rule"></div>
    <div class="brand-band">
      <div class="brand"><span class="brand-mark"></span>BRIGHTWELL ACADEMY</div>
      <div class="brand"><span class="brand-mark round"></span>VELTRIM HIRE</div>
      <div class="brand"><span class="brand-mark"></span>CORVANE ASSOCIATES</div>
    </div>
    <div class="cover-foot"></div>
  </section>

  <section class="spread" aria-label="Folder inside spread">
    <div class="panel left"></div>
    <div class="panel right"></div>
    <div class="fold"></div>
    <svg class="pocket" viewBox="0 0 318 147" aria-hidden="true">
      <path d="M15 0 H318 V147 H2 Z" fill="#1e8dcc"/>
      <path d="M15 0 H318 V3 H14.7 Z" fill="#3aa3d8"/>
    </svg>
    <div class="card">
      <div class="card-name">DANIEL MERCER</div>
      <div class="card-role">CEO</div>
      <div class="card-strip">
        <svg width="8" height="6" viewBox="0 0 8 6" aria-hidden="true"><rect x=".5" y=".5" width="7" height="5" fill="none" stroke="#e8e8e8"/><path d="M.5 .5 4 3.5 7.5 .5" fill="none" stroke="#e8e8e8"/></svg>
        <span>dan@lumenlead.org</span>
      </div>
    </div>
  </section>
</body>
</html>
```